Presentation of Business Project of Implementing CRM for a car Detailing Company

We need a professional PowerPoint presentation template (5 slides) for a business presentation about implementing a CRM system at Ravenmoor Detailing, a premium automotive detailing company in South Africa.
About the Company:
Ravenmoor Detailing specializes in high-end car detailing, paint protection, leather repair, and classic car restoration. They're a premium service provider looking to modernize their customer management through digital transformation.
What We Need:
A visually impressive presentation template with 5 key slide designs that we can duplicate and reuse across our full presentation. The presentation will show how a ChatterLoop-integrated CRM system can help the business grow from 60% to 80% customer retention, free up the owner's time, and enable expansion.
The 5 Slides:

Title slide - Space for project title + 5 team member names (impactful opening)
Content slide - Standard layout with bullet points (we'll duplicate this for 10+ slides)
Large data table - For vendor comparisons (4 rows × 10 columns)
Financial charts - 3 side-by-side scenario comparisons with bar/column charts
Simple table - For cost breakdowns (2-3 columns)

Design Style:
Modern, polished, and eye-catching. Should look professional but capture attention - think sleek automotive industry meets premium business consulting. Bold use of car detailing/workshop imagery as backgrounds where appropriate. Contemporary color scheme. Clean layouts that make data easy to read but NOT boring.

Images:
We will provide a link to high-quality car detailing and workshop images that you can integrate into the design (backgrounds, accents, visual interest).

https://www.filebarrow-share.example/drive/7kqLm2TzvPeXn9RwY4HsJ-bGD#RavenmoorDetailing

Link contain image of company actual work and logo of the company. The idea is to use their images.

Important:
All tables and charts should be editable so we can add our own data. Slides should be easy to duplicate and modify.

Deliverables:
5 PowerPoint slides (.pptx) - fully editable
Google Slides version
Fonts/colors consistent throughout

```html
<!DOCTYPE html>
<html lang="en">
<head>
<meta charset="utf-8">
<title>Ravenmoor Detailing – CRM Presentation Template</title>
<link rel="stylesheet" href="https://fonts.googleapis.com/css2?family=Montserrat:wght@700;800&family=Lato:wght@400;700&display=swap">
<style>
:root{
  --red:#f5202e;
  --red-mid:#f0444f;
  --red-soft:#f58a90;
  --ink:#0b0b0c;
  --ink-2:#141416;
  --row:#1a1a1c;
  --row-alt:#111113;
  --white:#ffffff;
  --muted:#cfcfd2;
  --page:#ffffff;
}
*{box-sizing:border-box;margin:0;padding:0}
html,body{width:1050px;height:1200px;overflow:hidden;background:var(--page)}
body{position:relative;font-family:"Lato",sans-serif;color:var(--white)}
.slide{position:absolute;width:453px;height:255px;background:radial-gradient(circle at 50% 40%,#17171a 0%,var(--ink) 75%);overflow:hidden}
.col-l{left:41px}.col-r{left:556px}
.row-1{top:41px}.row-2{top:329px}.row-3{top:616px}.row-4{top:904px}
.abs{position:absolute}
.page-no{position:absolute;left:0;bottom:0;width:20px;height:17px;background:var(--red);border-radius:0 10px 0 0;font-size:8px;font-weight:700;display:flex;align-items:center;justify-content:center}
.h{font-family:"Montserrat",sans-serif;font-weight:800;letter-spacing:.2px;line-height:1.15}
.red{color:var(--red)}
.rule{position:absolute;height:1.5px;width:22px;background:var(--red)}
.brand{position:absolute;display:flex;align-items:center;gap:4px;font-family:"Lato",sans-serif;font-weight:700;color:var(--white);letter-spacing:1px;white-space:nowrap}
.brand i{display:block;border-radius:50%;background:var(--red)}
.brand-sm{font-size:6.5px}.brand-sm i{width:8px;height:8px}
.lead{font-size:7.5px;color:var(--muted);text-align:center;line-height:1.5}
.bullets{position:absolute;list-style:none}
.bullets li{position:relative;padding-left:23px;font-size:9.4px;line-height:1.5;color:var(--white)}
.bullets li::before{content:"";position:absolute;left:1px;top:4px;width:8px;height:8px;border-radius:50%;border:1.6px solid var(--red);background:#2a2a2d}

/* title slide */
.s-title .brand{left:0;right:0;top:88px;justify-content:center;font-size:13px;letter-spacing:3px}
.s-title .brand i{width:12px;height:12px}
.s-title h1{position:absolute;top:136px;left:0;right:0;text-align:center;font-size:16.5px}
.s-title .sub{position:absolute;top:184px;left:0;right:0;text-align:center;font-size:9.4px}
.s-title .team{position:absolute;top:205px;left:0;right:0;text-align:center;font-size:8.6px;color:var(--red)}
.team span{margin:0 3px}

/* vendor table */
.vendor{position:absolute;left:25px;top:97px;width:403px;border-collapse:collapse;table-layout:fixed}
.vendor th{background:var(--red);height:18px;font-size:5.3px;font-weight:700;color:var(--white)}
.vendor th:first-child{font-size:8px;text-align:left;padding-left:9px;width:64px}
.vendor td{height:22px;font-size:4.9px;text-align:center;color:var(--muted);border-left:.6px solid #555}
.vendor td:first-child{font-size:7px;font-weight:700;color:var(--white);text-align:left;padding-left:11px;border-left:.6px solid #555}
.vendor tr:last-child td{border-bottom:.6px solid #555}
.vendor td:last-child{border-right:.6px solid #555}

/* charts */
.chart{position:absolute;top:98px;width:130px}
.chart h3{font-size:8px;font-weight:700;text-align:center;margin-bottom:6px;padding-right:18px}
.chart svg{display:block}

/* cost table */
.cost{position:absolute;left:34px;top:89px;width:385px;border-collapse:collapse}
.cost th{background:var(--red);height:18px;text-align:left;font-size:8px;font-weight:700;padding-left:11px}
.cost td{height:23px;font-size:8px;padding-left:11px;color:var(--white)}
.cost tr:nth-child(odd) td{background:var(--row)}
.cost tr:nth-child(even) td{background:var(--row-alt)}
.cost td:first-child{font-weight:700}
.cost .total td:first-child{color:var(--red)}

.photo{position:absolute;left:259px;top:16px;width:180px;height:224px;background:linear-gradient(150deg,#3b3e42 0%,#6d7176 38%,#2b2d30 70%,#151618 100%)}

.pair{position:absolute;font-size:9.4px;line-height:1.5;width:150px}
.pair::after{content:"";position:absolute;top:3px;width:8px;height:8px;border-radius:50%;border:1.6px solid var(--red);background:#2a2a2d}
.pair.l{left:41px}.pair.l::after{left:-21px}
.pair.r{right:51px;text-align:right}.pair.r::after{right:-22px}

.contact{position:absolute;top:196px;display:flex;align-items:center;gap:8px}
.contact .ico{width:24px;height:24px;border-radius:50%;background:var(--red);display:flex;align-items:center;justify-content:center}
.contact b{display:block;font-size:7.2px}
.contact span{font-size:6.8px}
</style>
</head>
<body>

<!-- 01 Title -->
<section class="slide col-l row-1 s-title">
  <div class="brand"><i></i>RAVENMOOR DETAILING</div>
  <h1 class="h">IMPLEMENTING A <span class="red">CHATTERLOOP-INTEGRATED</span><br><span class="red">CRM SYSTEM</span> AT RAVENMOOR DETAILING</h1>
  <p class="sub">Driving Customer Retention, Operational Efficiency &amp; Scalable Growth</p>
  <p class="team"><span>A. Mbeki-Lowe</span>-<span>I. Vosloo</span>-<span>S. Hartley</span>-<span>L. Dube</span>-<span>C. Marais</span></p>
</section>

<!-- 02 Content -->
<section class="slide col-l row-2">
  <h2 class="h abs" style="left:19px;top:17px;font-size:13.5px">WHY RAVENMOOR DETAILING NEEDS<br>A CHATTERLOOP-INTEGRATED CRM</h2>
  <div class="rule" style="left:19px;top:55px"></div>
  <div class="brand brand-sm" style="right:10px;top:44px"><i></i>RAVENMOOR</div>
  <ul class="bullets" style="left:19px;top:70px;width:380px">
    <li style="margin-bottom:9px">Customer retention currently sitting at ~60%, leaving growth capacity untapped</li>
    <li style="margin-bottom:9px">Customers prefer ChatterLoop for communication, booking, and follow-ups</li>
    <li style="margin-bottom:9px">Manual processes drain the owner’s time (estimates, reminders, scheduling)</li>
    <li style="margin-bottom:9px">CRM automation can centralize conversations, track jobs, and manage client history</li>
    <li style="margin-bottom:9px">Project goal: Increase retention to 80%+, free up 20–30 hrs/month, and enable business expansion</li>
    <li>Expected outcomes: smoother workflow, better customer experience, scalable operations</li>
  </ul>
  <div class="page-no">02</div>
</section>

<!-- 03 Vendor table -->
<section class="slide col-l row-3">
  <h2 class="h abs" style="left:0;right:0;top:23px;text-align:center;font-size:13.5px">COMPARING CHATTERLOOP-ENABLED CRM VENDORS</h2>
  <div class="rule" style="left:216px;top:45px"></div>
  <p class="lead abs" style="left:0;right:0;top:55px">Evaluating integration strength, automation capability, pricing, and suitability<br>for Ravenmoor Detailing’s growth goals.</p>
  <table class="vendor">
    <tr><th>Criteria</th><th>Vendor A</th><th>Vendor B</th><th>Vendor C</th><th>Vendor D</th><th>Vendor E</th><th>Vendor F</th><th>Vendor G</th><th>Vendor H</th><th>Vendor I</th><th>Vendor J</th></tr>
    <tr><td>ChatterLoop</td><td>Native</td><td>3rd-party</td><td>Native</td><td>Native</td><td>Limited</td><td>Native</td><td>Native</td><td>3rd-party</td><td>Native</td><td>Native</td></tr>
    <tr><td>Automation</td><td>Strong</td><td>Basic</td><td>Adv.</td><td>Moderate</td><td>Strong</td><td>Strong</td><td>Moderate</td><td>Adv.</td><td>Strong</td><td>Basic</td></tr>
    <tr><td>Price</td><td>R1200</td><td>R950</td><td>R1800</td><td>R1500</td><td>R550</td><td>R1200</td><td>R2100</td><td>R1100</td><td>R1350</td><td>R900</td></tr>
    <tr><td>Best For</td><td>Growth</td><td>Budget</td><td>Heavy use</td><td>Teams</td><td>Starters</td><td>Growth</td><td>Growth</td><td>Custom</td><td>Scaling</td><td>Essentials</td></tr>
  </table>
  <div class="page-no">03</div>
</section>

<!-- 04 Charts -->
<section class="slide col-l row-4">
  <h2 class="h abs" style="left:0;right:0;top:23px;text-align:center;font-size:13.5px">THREE-SCENARIO FINANCIAL BREAKDOWN</h2>
  <div class="rule" style="left:216px;top:45px"></div>
  <p class="lead abs" style="left:0;right:0;top:55px">Evaluating integration strength, automation capability, pricing, and suitability<br>for Ravenmoor Detailing’s growth goals.</p>

  <div class="chart" style="left:18px">
    <h3>Customer Retention</h3>
    <svg width="130" height="110" viewBox="0 0 130 110" font-family="Lato, sans-serif" font-size="4.5" fill="#cfcfd2">
      <g><text x="0" y="20">500</text><text x="0" y="35">400</text><text x="0" y="50">300</text><text x="0" y="66">200</text><text x="0" y="81">100</text><text x="2" y="96">0</text></g>
      <rect x="18" y="75" width="21" height="20" fill="#f5202e"/>
      <rect x="43" y="60" width="21" height="35" fill="#f0444f"/>
      <rect x="68" y="44" width="21" height="51" fill="#f5202e"/>
      <rect x="92" y="28" width="21" height="67" fill="#f58a90"/>
      <path d="M20 62 Q40 54 55 45 T78 28 T104 15 L115 12" fill="none" stroke="#fff" stroke-width=".7"/>
      <path d="M111 10 L115 12 L112 15" fill="none" stroke="#fff" stroke-width=".7"/>
      <g fill="#f5202e"><circle cx="29" cy="61" r="2.4"/><circle cx="53" cy="46" r="2.4"/><circle cx="78" cy="29" r="2.4"/><circle cx="102" cy="16" r="2.4"/></g>
      <g><text x="25" y="105">30%</text><text x="50" y="105">4%</text><text x="74" y="105">60%</text><text x="98" y="105">80%</text></g>
    </svg>
  </div>

  <div class="chart" style="left:167px">
    <h3>Repeat Revenue</h3>
    <svg width="130" height="110" viewBox="0 0 130 110" font-family="Lato, sans-serif" font-size="4.5" fill="#cfcfd2">
      <g><text x="0" y="20">500</text><text x="0" y="35">400</text><text x="0" y="50">300</text><text x="0" y="66">200</text><text x="0" y="81">100</text><text x="2" y="96">0</text></g>
      <rect x="18" y="75" width="21" height="20" fill="#f5202e"/>
      <rect x="43" y="60" width="21" height="35" fill="#2b2b2e"/>
      <rect x="68" y="44" width="21" height="51" fill="#f5202e"/>
      <rect x="92" y="28" width="21" height="67" fill="#1c1c1e"/>
      <path d="M20 62 Q40 54 55 45 T78 28 T104 15 L115 12" fill="none" stroke="#fff" stroke-width=".7"/>
      <path d="M111 10 L115 12 L112 15" fill="none" stroke="#fff" stroke-width=".7"/>
      <g fill="#f5202e"><circle cx="29" cy="61" r="2.4"/><circle cx="53" cy="46" r="2.4" fill="#555"/><circle cx="78" cy="29" r="2.4"/></g>
      <g><text x="25" y="105">30%</text><text x="50" y="105">4%</text><text x="74" y="105">60%</text><text x="98" y="105">80%</text></g>
    </svg>
  </div>

  <div class="chart" style="left:316px">
    <h3>Owner Time Saved</h3>
    <svg width="130" height="110" viewBox="0 0 130 110" font-family="Lato, sans-serif" font-size="4.5" fill="#cfcfd2">
      <g><text x="0" y="20">500</text><text x="0" y="35">400</text><text x="0" y="50">300</text><text x="0" y="66">200</text><text x="0" y="81">100</text><text x="2" y="96">0</text></g>
      <rect x="18" y="75" width="21" height="20" fill="#f5202e"/>
      <rect x="43" y="60" width="21" height="35" fill="#f0444f"/>
      <rect x="68" y="44" width="21" height="51" fill="#f5202e"/>
      <rect x="92" y="28" width="21" height="67" fill="#f58a90"/>
      <path d="M20 62 Q40 54 55 45 T78 28 T104 15 L115 12" fill="none" stroke="#fff" stroke-width=".7"/>
      <path d="M111 10 L115 12 L112 15" fill="none" stroke="#fff" stroke-width=".7"/>
      <g fill="#f5202e"><circle cx="29" cy="61" r="2.4"/><circle cx="53" cy="46" r="2.4"/><circle cx="78" cy="29" r="2.4"/><circle cx="102" cy="16" r="2.4"/></g>
      <g><text x="25" y="105">30%</text><text x="50" y="105">4%</text><text x="74" y="105">60%</text><text x="98" y="105">80%</text></g>
    </svg>
  </div>
  <div class="page-no">04</div>
</section>

<!-- 05 Cost table -->
<section class="slide col-r row-1">
  <h2 class="h abs" style="left:0;width:453px;top:31px;text-align:center;font-size:13.5px">CRM INVESTMENT OVERVIEW</h2>
  <div class="rule" style="left:216px;top:52px"></div>
  <div class="brand brand-sm" style="right:9px;top:43px"><i></i>RAVENMOOR</div>
  <p class="lead abs" style="left:0;right:0;top:63px;color:var(--white)">Overview of once-off and monthly costs required to implement the CRM system.</p>
  <table class="cost">
    <tr><th style="width:129px">Item</th><th style="width:125px">Monthly Cost</th><th>Notes</th></tr>
    <tr><td>CRM Subscription</td><td>R__</td><td>Based on chosen vendor</td></tr>
    <tr><td>ChatterLoop Business API</td><td>R__</td><td>Pay-per-message or bundle</td></tr>
    <tr><td>Onboarding &amp; Setup</td><td>Once-off R__</td><td>Workflow + automation setup</td></tr>
    <tr><td>Training</td><td>R__</td><td>Staff training session</td></tr>
    <tr class="total"><td>Total</td><td>R__</td><td>Expected ROI in 3–6 months</td></tr>
  </table>
  <div class="page-no">05</div>
</section>

<!-- 06 Content with photo -->
<section class="slide col-r row-2">
  <h2 class="h abs" style="left:19px;top:17px;font-size:13.5px">PROPOSED SOLUTION</h2>
  <div class="rule" style="left:19px;top:40px"></div>
  <ul class="bullets" style="left:19px;top:55px;width:225px">
    <li style="margin-bottom:7px">Customer retention currently sitting at ~60%, leaving growth capacity untapped</li>
    <li style="margin-bottom:7px">Manual processes drain the owner’s time (estimates, reminders, scheduling)</li>
    <li style="margin-bottom:7px">CRM automation can centralize conversations, track jobs, and manage client history</li>
    <li style="margin-bottom:7px">Project goal: Increase retention to 80%+, free up 20–30 hrs/month, and enable business expansion</li>
    <li>Expected outcomes: smoother workflow, better customer experience, scalable</li>
  </ul>
  <div class="photo" role="img" aria-label="Photo of a gloved detailer machine-polishing the paint of a dark car"></div>
  <div class="page-no">06</div>
</section>

<!-- 07 Problem / solution -->
<section class="slide col-r row-3">
  <h2 class="h abs" style="left:0;right:0;top:21px;text-align:center;font-size:13.5px">PROPOSED SOLUTION</h2>
  <div class="rule" style="left:216px;top:44px"></div>
  <p class="pair l" style="top:73px">Customer retention stuck<br>at ~60%</p>
  <p class="pair l" style="top:111px">Manual follow-ups lead to<br>missed bookings</p>
  <p class="pair l" style="top:154px">Owner spends too much time<br>on admin tasks</p>
  <p class="pair r" style="top:73px">Builds stronger customer<br>relationships</p>
  <p class="pair r" style="top:111px">Inconsistent response times<br>on ChatterLoop</p>
  <p class="pair r" style="top:154px">Customer retention stuck<br>at ~60%</p>
  <div class="brand" style="left:0;right:0;top:100px;justify-content:center;font-size:8px;flex-direction:column;gap:6px"><i style="width:46px;height:46px"></i>RAVENMOOR</div>
  <p class="abs" style="left:0;right:0;top:188px;text-align:center;font-size:9.4px;line-height:1.5">Faster response times lead to<br>more bookings</p>
  <div class="page-no">07</div>
</section>

<!-- 08 Closing -->
<section class="slide col-r row-4">
  <div class="brand" style="left:0;right:0;top:102px;justify-content:center;font-size:13px;letter-spacing:3px"><i style="width:12px;height:12px"></i>RAVENMOOR DETAILING</div>
  <h2 class="h abs" style="left:0;right:0;top:135px;text-align:center;font-size:17px">THANK <span class="red">YOU</span></h2>
  <p class="abs" style="left:0;right:0;top:163px;text-align:center;font-size:9.4px">Driving Customer Retention, Operational Efficiency &amp; Scalable Growth</p>
  <div class="contact" style="left:52px">
    <div class="ico"><svg width="12" height="9" viewBox="0 0 12 9"><rect x=".5" y=".5" width="11" height="8" fill="none" stroke="#fff"/><path d="M.5 .5 L6 5 L11.5 .5" fill="none" stroke="#fff"/></svg></div>
    <div><b>Call Us</b><span>+27 72 555 0184</span></div>
  </div>
  <div class="contact" style="left:174px">
    <div class="ico"><svg width="11" height="11" viewBox="0 0 24 24"><path fill="#fff" d="M6.6 10.8a15 15 0 0 0 6.6 6.6l2.2-2.2a1 1 0 0 1 1-.25 11 11 0 0 0 3.6.6 1 1 0 0 1 1 1V20a1 1 0 0 1-1 1A17 17 0 0 1 3 4a1 1 0 0 1 1-1h3.5a1 1 0 0 1 1 1 11 11 0 0 0 .6 3.6 1 1 0 0 1-.25 1z"/></svg></div>
    <div><b>Email</b><span>hello@ravenmoor.example</span></div>
  </div>
  <div class="contact" style="left:307px">
    <div class="ico"><svg width="12" height="12" viewBox="0 0 12 12" fill="none" stroke="#fff" stroke-width=".9"><circle cx="6" cy="6" r="5"/><ellipse cx="6" cy="6" rx="2.2" ry="5"/><path d="M1 6h10M2 3.3h8M2 8.7h8"/></svg></div>
    <div><b>Website</b><span>www.ravenmoor.example</span></div>
  </div>
</section>

</body>
</html>
```